Brightwell Ledger - fund management and algorithmic design

We're looking for a web design for a new company called brightwell ledger which is based out of London.

The photography provided will be a major part of the creative content. The intent is to have a sharp, clear, professional, slick look. Less is more and clutter is not the root that should be followed.

A logo has been selected and the photography provided will give the designer a good idea of what we are looking for. The logo designer is still getting back to me with the very final version but what is provided is good enough to move forward with. the final design will likely have this changed slightly.

The photos are about 1.2 meg each at 86 pdi. I believe this is about right for a high quality web image.

At some point on the site it should have: Integrity, Innovative, Progressive. These are core principles of the company. Also ,Fund management and algorithmic design could be used somewhere as this explains exactly what we do.

I also wish to have the secondary pages designed too. However, rather than asking everybody to do this i will ask a select few designers to look at one of the pages. The chosen designer will then be asked to finish the other pages too. These are expected to be quite simple, nothing fussy - clean and presentable with a small amount of room for artistic license.

Also the links to these two sites will give you a very good idea of what we're looking for.

ternovix.com
quilbrookpartners.com
vellingtonpeakfx.com

Hi,

sorry for as i had problem getting the final images from the photographer as he's been away and busy.

However, we now the the logo (be it not the very final version) and the photos uploaded.  Please read the brief again as this has been updated too.

Initially i'd be happy if you made up the front page and after that i will ask a small handful of designers to submit a design for the secondary page - this way i feel is better as it uses less of your time.  These pages are likely to use the photography for a backdrop too.

Looking forward to your designs.

Regards,

Neville

Reason: I have extended the deadline as the first week has been held up because of delays in content. thanks, Neville

Target Market(s)

wealth individuals who wish to diversify their investment portfolios with investments predominantly in the foreign exchange markets as well as some financial products offered by DRAVExchange.com

Industry/Entity Type

It Company

Requirements
Must have
• There are three photos that the site must use, once the final design is fully operational and coded we want the first three photos to rotate on the front page. Much like ternovix.com

An area where a prospective client can enter their email address to receive market new letters and correspondences from brightwell ledger.

front page

about us,
managed accounts
systems and performance

```html
<!DOCTYPE html>
<html lang="en">
<head>
<meta charset="utf-8">
<title>Brightwell Ledger – Fund management and algorithmic design</title>
<link rel="stylesheet" href="https://fonts.googleapis.com/css2?family=Open+Sans:wght@400;600&display=swap">
<style>
  :root {
    --accent: #0aa5e0;
    --ink: #333333;
    --ink-soft: #777777;
    --heading: #222222;
    --nav-text: #ffffff;
    --header-bg: rgba(40, 40, 42, 0.92);
    --hero-deep: #0c0907;
    --hero-mid: #2a201a;
    --hero-glow: #3b4a66;
    --icon-dark: #4a4a4a;
    --rule: #d6d6d6;
    --page: #ffffff;
  }
  * { margin: 0; padding: 0; box-sizing: border-box; }
  html, body { width: 865px; height: 1200px; overflow: hidden; background: var(--page); }
  body { position: relative; font-family: "Open Sans", Arial, sans-serif; color: var(--ink); }
  a { color: inherit; text-decoration: none; }

  .hero {
    position: absolute; left: 0; top: 0; width: 865px; height: 580px;
    background:
      radial-gradient(ellipse 380px 200px at 50% 75%, rgba(59,74,102,0.55), transparent 70%),
      radial-gradient(ellipse 300px 260px at 22% 45%, rgba(120,110,100,0.35), transparent 70%),
      radial-gradient(ellipse 260px 240px at 65% 40%, rgba(120,110,100,0.3), transparent 70%),
      linear-gradient(180deg, var(--hero-mid) 0%, #1c1612 55%, var(--hero-deep) 100%);
    border-bottom: 4px solid #000;
  }
  .hero-thumbs { position: absolute; left: 306px; top: 532px; display: flex; gap: 2px; }
  .hero-thumb { width: 64px; height: 42px; border: 1px solid #9a9a9a; }
  .hero-thumb--one { background: linear-gradient(135deg, #6a6a6a, #2a2a2a); }
  .hero-thumb--two { background: linear-gradient(135deg, #3c5566, #1b2630); }
  .hero-thumb--three { background: linear-gradient(135deg, #5a7fb8, #2c3a5c); }
  .hero-thumb--four { background: linear-gradient(135deg, #4a3e34, #1a1612); }

  .site-header {
    position: absolute; left: 0; top: 0; width: 865px; height: 86px;
    background: var(--header-bg);
  }
  .brand {
    position: absolute; left: 92px; top: 31px;
    font-size: 17px; font-weight: 400; color: var(--nav-text); letter-spacing: 0.3px;
  }
  .main-nav { position: absolute; left: 372px; top: 36px; display: flex; gap: 0; }
  .main-nav a { font-size: 11.5px; color: var(--nav-text); margin-right: 24px; padding-bottom: 5px; }
  .main-nav a.is-active { color: var(--accent); border-bottom: 1px solid var(--accent); }
  .main-nav a:last-child { margin-right: 0; }

  .about { position: absolute; left: 0; top: 624px; width: 865px; text-align: center; }
  .about h2 { font-size: 19px; font-weight: 400; color: var(--heading); margin-bottom: 14px; }
  .about p { font-size: 11px; line-height: 13px; width: 640px; margin: 0 auto; }
  .about p.lead { margin-bottom: 7px; }
  .read-more { display: inline-block; font-size: 11px; color: var(--accent); }
  .about .read-more { margin-top: 6px; }

  .divider { position: absolute; left: 130px; top: 786px; width: 604px; height: 1px; background: var(--rule); }
  .divider-mark { position: absolute; left: 427px; top: 781px; width: 11px; height: 11px; background: var(--page); }

  .services { position: absolute; left: 0; top: 826px; width: 865px; }
  .service { position: absolute; top: 0; width: 210px; text-align: center; }
  .service--accounts { left: 89px; }
  .service--systems { left: 329px; }
  .service--performance { left: 563px; }
  .service-icon { display: block; margin: 0 auto; width: 56px; height: 56px; }
  .service h3 { font-size: 14px; font-weight: 400; color: var(--heading); margin: 18px 0 14px; }
  .service p { font-size: 11px; line-height: 13px; }
  .service p + p { margin-top: 5px; }
  .service .read-more { margin-top: 24px; }

  .footer-shadow {
    position: absolute; left: 54px; top: 1090px; width: 750px; height: 10px;
    background: radial-gradient(ellipse 50% 100% at 50% 0%, rgba(0,0,0,0.28), transparent 80%);
  }
  .site-footer { position: absolute; left: 98px; top: 1127px; width: 671px; font-size: 9.5px; color: var(--ink-soft); }
  .footer-links { position: absolute; right: 0; top: 0; display: flex; gap: 19px; }
</style>
</head>
<body>
  <div class="hero" role="img" aria-label="Night photograph of a lit Victorian bascule bridge over the river with a city skyline behind">
    <div class="hero-thumbs">
      <div class="hero-thumb hero-thumb--one" role="img" aria-label="Slide thumbnail: city street"></div>
      <div class="hero-thumb hero-thumb--two" role="img" aria-label="Slide thumbnail: glass tower at dusk"></div>
      <div class="hero-thumb hero-thumb--three" role="img" aria-label="Slide thumbnail: city skyline by day"></div>
      <div class="hero-thumb hero-thumb--four" role="img" aria-label="Slide thumbnail: bridge at night"></div>
    </div>
  </div>

  <header class="site-header">
    <a class="brand" href="#">Brightwell Ledger</a>
    <nav class="main-nav">
      <a class="is-active" href="#">Home</a>
      <a href="#">About us</a>
      <a href="#">Financials</a>
      <a href="#">Intelligence</a>
      <a href="#">Technology</a>
      <a href="#">Contact</a>
    </nav>
  </header>

  <section class="about">
    <h2>About us</h2>
    <p class="lead">Lorem ipsum dolor sit amet, consectetur adipisicing elit, sed do eiusmod tempor incididunt</p>
    <p>ut labore et dolore magna aliqua. Ut enim ad minim veniam, quis nostrud exercitation ullamco laboris nisi ut aliquip ex ea commodo consequat. Duis aute irure dolor in reprehenderit in voluptate velit esse cillum dolore eu fugiat nulla pariatur. Excepteur sint occaecat cupidatat non proident, sunt in culpa qui officia deserunt mollit anim id est laborum.exercitation ullamco laboris nisi ut aliquip ex ea commodo consequat.</p>
    <a class="read-more" href="#">Read More</a>
  </section>

  <div class="divider"></div>
  <svg class="divider-mark" viewBox="0 0 11 11" aria-hidden="true">
    <rect x="1" y="1" width="4" height="4" fill="#0aa5e0"/><rect x="6" y="1" width="4" height="4" fill="#0aa5e0"/>
    <rect x="1" y="6" width="4" height="4" fill="#0aa5e0"/><rect x="6" y="6" width="4" height="4" fill="#0aa5e0"/>
  </svg>

  <section class="services">
    <article class="service service--accounts">
      <svg class="service-icon" viewBox="0 0 56 56" aria-hidden="true">
        <circle cx="28" cy="28" r="26.5" fill="#fff" stroke="#444" stroke-width="1.5"/>
        <rect x="13" y="19" width="30" height="20" rx="1.5" fill="#0aa5e0"/>
        <circle cx="21" cy="16" r="4" fill="#0aa5e0"/>
        <rect x="16" y="25" width="8" height="9" fill="#fff"/>
        <rect x="27" y="25" width="12" height="2" fill="#fff"/>
        <rect x="27" y="29" width="12" height="2" fill="#fff"/>
        <rect x="27" y="33" width="9" height="2" fill="#fff"/>
        <path d="M30 40 v8 l2-2 l2 4 l2-1 l-2-4 h3 z" fill="#fff" stroke="#333" stroke-width="1"/>
      </svg>
      <h3>Managed Accounts</h3>
      <p>Lorem ipsum dolor sit amet, consectetur adipisicing elit,</p>
      <p>labore et dolore magna aliqua. Ut enim ad minim veniam, quis nostrud exercitation ullamco laboris nisi ut aliquip ex ea commodo .</p>
      <a class="read-more" href="#">Read More</a>
    </article>

    <article class="service service--systems">
      <svg class="service-icon" viewBox="0 0 56 56" aria-hidden="true">
        <circle cx="28" cy="28" r="27" fill="#4a4a4a"/>
        <g fill="#fff" transform="translate(28 28)">
          <rect x="-3" y="-16" width="6" height="7"/>
          <rect x="-3" y="-16" width="6" height="7" transform="rotate(45)"/>
          <rect x="-3" y="-16" width="6" height="7" transform="rotate(90)"/>
          <rect x="-3" y="-16" width="6" height="7" transform="rotate(135)"/>
          <rect x="-3" y="-16" width="6" height="7" transform="rotate(180)"/>
          <rect x="-3" y="-16" width="6" height="7" transform="rotate(225)"/>
          <rect x="-3" y="-16" width="6" height="7" transform="rotate(270)"/>
          <rect x="-3" y="-16" width="6" height="7" transform="rotate(315)"/>
          <circle r="11"/>
        </g>
        <circle cx="28" cy="28" r="5" fill="#4a4a4a"/>
      </svg>
      <h3>Systems</h3>
      <p>Lorem ipsum dolor sit amet, consectetur adipisicing elit,</p>
      <p>labore et dolore magna aliqua. Ut enim ad minim veniam, quis nostrud exercitation ullamco laboris nisi ut aliquip ex ea commodo.</p>
      <a class="read-more" href="#">Read More</a>
    </article>

    <article class="service service--performance">
      <svg class="service-icon" viewBox="0 0 56 56" aria-hidden="true">
        <circle cx="28" cy="28" r="27" fill="#4a4a4a"/>
        <path d="M12 34 A16 16 0 0 1 44 34" fill="none" stroke="#fff" stroke-width="2" stroke-dasharray="2 3"/>
        <path d="M28 32 L40 20 L42 22 L30 34 Z" fill="#fff"/>
        <circle cx="28" cy="33" r="3" fill="#fff"/>
        <circle cx="44" cy="14" r="2" fill="#fff"/>
      </svg>
      <h3>Performance</h3>
      <p>Lorem ipsum dolor sit amet, consectetur adipisicing elit,</p>
      <p>labore et dolore magna aliqua. Ut enim ad minim veniam, quis nostrud exercitation ullamco laboris nisi ut aliquip ex ea commodo.</p>
      <a class="read-more" href="#">Read More</a>
    </article>
  </section>

  <div class="footer-shadow"></div>
  <footer class="site-footer">
    <span>Copyright © 2011 - 2013 Company Name</span>
    <nav class="footer-links">
      <a href="#">Contact</a>
      <a href="#">Terms of Use</a>
      <a href="#">Privacy</a>
    </nav>
  </footer>
</body>
</html>
```